Bright Path Flyer Design for Virtual Online Clinic. -5.5 x 8.5 inches (half sheet)

We need a clean, modern flyer design for Bright Path, a new virtual walk-in clinic based in British Columbia. The flyer will be used in libraries, pharmacies, and community centers to help residents easily access primary care through their Bright Path NFC access card.
The flyer will ask a question : NEED A DOCTOR? This should be large and attention grabbing.
The design should clearly feature a Bright Path card image (the access card) as the centerpiece and visually show how patients can use it to book appointments. The tone should feel trustworthy, healthcare-oriented, and community-friendly — clean fonts, clear spacing, and strong readability from a distance.

Side One: This card has the NFC Access Card.
NEED A DOCTOR? (Large Font, Attention Grabbing)
How to Book an Appointment using your Bright Path Card
Step 1: Tap Your Card on Your Phone
Hold your card near the back of your phone.
It will activate automatically — no app needed.
The Bright Path scheduler will open.
Step 2: Schedule Your Appointment
Select your clinical concern.
Choose your time window.
Register (only once).
Confirm your appointment.
Step 3: Relax, we’ll take care of the rest
A doctor will call during your scheduled time.
Once booked, you’ll be able to call our office.
No emails, no texts — just a real person.
It’s that simple.
Side Two:
About Bright Path
Created by Dr. Marcus Ferrigan
Bright Path was founded to make healthcare simple and convenient. Prescription renewals. Common infections. Medical notes. And so much more.
Our doctors can address 120+ health concerns virtually — providing quality care without the waiting room. No waiting rooms. Just real doctors providing real care.
Why Patients Choose Bright Path
Easy access – book and be seen from anywhere in BC.
Effortless booking – tap your Bright Path Card to begin.
Trusted physicians – every visit is with a licensed BC family doctor.
How It Works
Book your visit — choose a time window that fits your day.
Join the queue — you’ll be called when it’s your turn.
Speak directly with your doctor — simple, secure, and stress-free.
Convenient Care for Common Concerns

Additional Details.
Please find the domain to be launched soon. I've attached the NFC card file for review, it is 85.5 mm x 54 mm. The card will be glued to the flyer.
I've attached examples of flyers but they are not the look I am seeking and I am looking for creative solutions.
Thank you!
http://brightpath-example.test/

Adult Patients in British Columbia

Healthcare

• Looking for clean lines, uniform appearance, and high legibility i.e poppins

0054AA
0677BA
7BADD7
CADEEF
E8F1F8

• Need A Doctor?
• Elegant style, not too busy, clear layout.
• Clutter, look cheap - review examples.

```html
<!DOCTYPE html>
<html lang="en">
<head>
<meta charset="utf-8">
<title>Bright Path – Flyer, Side One and Side Two</title>
<link rel="stylesheet" href="https://fonts.googleapis.com/css2?family=Oswald:wght@200;700&family=Poppins:wght@300;400;500;600;700&display=swap">
<style>
  :root{
    --backdrop:#e4e4e4;
    --brand:#2c4592;
    --brand-deep:#233a80;
    --paper:#ffffff;
    --panel:#eef0f4;
    --muted:#8b8e97;
    --muted-light:#a5a8b0;
    --skin:#f3b27a;
  }
  *{box-sizing:border-box;margin:0;padding:0}
  html,body{width:1200px;height:3223px;overflow:hidden;background:var(--backdrop)}
  body{position:relative;font-family:"Poppins",sans-serif}

  .flyer{position:absolute;left:294px;width:612px;background:var(--paper);overflow:hidden;
    box-shadow:0 6px 14px rgba(0,0,0,.16)}
  .flyer--front{top:677px;height:897px}
  .flyer--back{top:1623px;height:923px}
  .abs{position:absolute}

  /* ---------- Side one ---------- */
  .hero{left:0;top:0;width:612px;height:559px;background:var(--brand)}
  .headline-light{left:54px;top:24px;font-family:"Oswald",sans-serif;font-weight:200;font-size:108px;line-height:1;color:#fff;letter-spacing:-1px}
  .headline-bold{left:52px;top:120px;font-family:"Oswald",sans-serif;font-weight:700;font-size:148px;line-height:1;color:#fff;letter-spacing:-4px}
  .brand-mark{left:382px;top:46px;display:flex;align-items:center;gap:10px;color:#fff;font-weight:500;font-size:26px;letter-spacing:.5px}
  .brand-mark .dot{width:14px;height:14px;border-radius:50%;background:#fff}
  .card-scene{left:0;top:283px;width:551px;height:276px}
  .book-bubble{left:347px;top:342px;width:231px;height:135px;border:2px solid #fff;border-radius:16px;background:var(--brand);
    color:#fff;text-align:center;font-size:15.5px;line-height:1.25;padding-top:16px}
  .book-bubble .tag{display:inline-block;background:#fff;color:var(--brand);font-weight:700;font-size:16px;padding:2px 12px;margin:6px 0 8px}
  .nfc-pill{left:238px;top:493px;width:269px;height:46px;border:2px solid #fff;border-radius:23px;background:var(--brand);
    display:flex;align-items:center;color:#fff;font-size:13px;line-height:1.15}
  .nfc-pill .chip{width:26px;height:26px;border:2px solid #fff;border-radius:4px;margin:0 20px 0 34px}
  .nfc-pill b{font-weight:600}

  .steps-art{left:-50px;top:596px;width:262px;height:262px;border-radius:50%;background:#ececf1}
  .steps-art-figure{left:10px;top:632px;width:120px;height:200px;border-radius:18px;
    background:linear-gradient(160deg,#2c4592 0%,#2c4592 38%,var(--skin) 40%,#f6c597 100%);opacity:.9}
  .step-badge{width:62px;height:62px;border-radius:50%;border:3px solid var(--brand);background:#fff;color:var(--brand);
    text-align:center;line-height:1}
  .step-badge small{display:block;font-size:9px;font-weight:500;margin-top:9px;letter-spacing:.5px}
  .step-badge strong{display:block;font-size:25px;font-weight:700;margin-top:1px}
  .step-rule{height:0;border-top:1.5px dashed #9aa3bd}
  .step-list{list-style:none;color:var(--brand);font-size:10.2px;font-weight:500;line-height:16.6px}
  .step-list li::before{content:"•";margin-right:8px}

  /* ---------- Side two ---------- */
  .about-band{left:0;top:0;width:612px;height:407px;background:var(--brand)}
  .about-light{left:64px;top:36px;font-family:"Oswald",sans-serif;font-weight:200;font-size:64px;line-height:1;color:#fff}
  .about-bold{left:63px;top:92px;font-family:"Oswald",sans-serif;font-weight:700;font-size:91px;line-height:1;color:#fff;letter-spacing:-1px}
  .creator-pill{left:63px;top:200px;width:411px;height:44px;border:2px solid #fff;border-radius:22px;display:flex;align-items:stretch;overflow:hidden}
  .creator-pill span{display:flex;align-items:center;padding-left:16px;width:141px;color:#fff;font-size:19px}
  .creator-pill b{flex:1;display:flex;align-items:center;justify-content:center;background:#fff;border-radius:22px;color:var(--brand);font-size:19px;font-weight:700}
  .about-copy{left:64px;width:420px;color:#fff;font-size:13.4px;line-height:17.5px}

  .why-panel{left:50px;top:443px;width:527px;height:258px;border-radius:14px;background:var(--panel)}
  .why-title{left:81px;top:459px;color:var(--brand);line-height:1.05}
  .why-title .light{display:block;font-size:30px;font-weight:400}
  .why-title .bold{display:block;font-size:22px;font-weight:700}
  .reason{top:548px;width:145px;height:131px;border-radius:8px;background:#fff;padding:14px 0 0 19px}
  .reason h3{font-size:17px;font-weight:500;color:var(--muted);line-height:1.1}
  .reason hr{border:0;border-top:1px solid #dcdde2;width:95px;margin:8px 0 10px}
  .reason p{font-size:12px;color:var(--muted-light);line-height:1.25;padding-right:12px}

  .how-box{left:53px;top:751px;width:509px;height:140px;border:1.5px solid var(--brand);border-radius:12px}
  .how-tab{left:188px;top:728px;width:237px;height:42px;border-radius:8px;background:var(--brand);color:#fff;
    display:flex;align-items:center;justify-content:center;font-weight:700;font-size:21px}
  .how-list{left:81px;top:790px;list-style:none;color:var(--muted);font-size:13px;line-height:21px}
  .how-list li::before{content:"•";margin-right:13px;color:var(--muted-light)}
</style>
</head>
<body>

<!-- Side one -->
<section class="flyer flyer--front">
  <div class="abs hero"></div>
  <div class="abs headline-light">NEED A</div>
  <h1 class="abs headline-bold">DOCTOR?</h1>
  <div class="abs brand-mark"><span class="dot"></span>Bright Path</div>

  <svg class="abs card-scene" viewBox="0 0 551 276" role="img" aria-label="Illustration: a hand holding the Bright Path access card next to a smartphone">
    <defs>
      <linearGradient id="sceneTone" x1="0" y1="0" x2="1" y2="0">
        <stop offset="0" stop-color="#f3b27a" stop-opacity=".55"/>
        <stop offset=".5" stop-color="#ffffff" stop-opacity=".35"/>
        <stop offset="1" stop-color="#1b1f2a" stop-opacity=".55"/>
      </linearGradient>
    </defs>
    <rect x="0" y="0" width="551" height="276" rx="0" fill="url(#sceneTone)"/>
  </svg>

  <div class="abs book-bubble">
    How to Book an<br>
    <span class="tag">Appointment</span><br>
    Using your<br>Bright Path Card
  </div>

  <div class="abs nfc-pill"><span class="chip"></span><span>This card has the<br><b>NFC Access Card.</b></span></div>

  <div class="abs steps-art" role="img" aria-label="Illustration: a hand tapping the card against a phone"></div>
  <div class="abs steps-art-figure" role="img" aria-label="Illustration: hands holding a phone with the card"></div>

  <div class="abs step-badge" style="left:112px;top:585px"><small>STEP</small><strong>01</strong></div>
  <div class="abs step-rule" style="left:176px;top:616px;width:106px"></div>
  <ul class="abs step-list" style="left:304px;top:578px">
    <li>Tap Your Card on Your Phone</li>
    <li>Hold Your Card Near The Back Of Your Phone</li>
    <li>It will activate automatically — no app needed.</li>
    <li>The Bright Path scheduler will open.</li>
  </ul>

  <div class="abs step-badge" style="left:172px;top:690px"><small>STEP</small><strong>02</strong></div>
  <div class="abs step-rule" style="left:236px;top:721px;width:152px"></div>
  <ul class="abs step-list" style="left:412px;top:678px">
    <li>Schedule Your Appointment</li>
    <li>Select your clinical concern.</li>
    <li>Choose your time window.</li>
    <li>Register (only once).</li>
    <li>Confirm your appointment.</li>
  </ul>

  <div class="abs step-badge" style="left:112px;top:799px"><small>STEP</small><strong>03</strong></div>
  <div class="abs step-rule" style="left:176px;top:830px;width:103px"></div>
  <ul class="abs step-list" style="left:304px;top:787px">
    <li>Relax, We'll Take Care Of The Rest</li>
    <li>A Doctor Will Call During Your Scheduled Time.</li>
    <li>Once Booked, You'll Be Able To Call Our Office.</li>
    <li>No Emails, No Texts — Just A Real Person.</li>
    <li>It's That Simple.</li>
  </ul>
</section>

<!-- Side two -->
<section class="flyer flyer--back">
  <div class="abs about-band"></div>
  <div class="abs about-light">ABOUT</div>
  <h2 class="abs about-bold">BRIGHT PATH</h2>
  <div class="abs creator-pill"><span>Created by</span><b>Dr. Marcus Ferrigan</b></div>
  <p class="abs about-copy" style="top:272px">Bright Path was founded to make healthcare simple and convenient. Prescription renewals. Common infections. Medical notes. And so much more.</p>
  <p class="abs about-copy" style="top:335px">Our doctors can address 120+ health concerns virtually providing quality care without the waiting room. No waiting rooms. Just real doctors providing real care.</p>

  <div class="abs why-panel"></div>
  <h3 class="abs why-title"><span class="light">WHY PATIENTS?</span><span class="bold">CHOOSE BRIGHT PATH</span></h3>
  <div class="abs reason" style="left:75px"><h3>Easy<br>Access</h3><hr><p>Book and Be Seen From Anywhere In BC.</p></div>
  <div class="abs reason" style="left:240px"><h3>Effortless<br>Booking</h3><hr><p>Tap your Bright Path Card to begin.</p></div>
  <div class="abs reason" style="left:407px"><h3>Trusted<br>Physicians</h3><hr><p>Every visit is with a licensed BC family doctor.</p></div>

  <div class="abs how-box"></div>
  <div class="abs how-tab">HOW IT WORKS</div>
  <ul class="abs how-list">
    <li>Book your visit — choose a time window that fits your day.</li>
    <li>Join the queue — you'll be called when it's your turn.</li>
    <li>Speak directly with your doctor — simple, secure, and stress-free.</li>
    <li>Convenient Care for Common Concerns</li>
  </ul>
</section>

</body>
</html>
```